Copper Ridge Resort & Marina - Boat Slips, Cabin Rentals, Floating Vacation Homes, & More

We need an 8'H x 16'W billboard for our Resort & marina, www.copperridgeresort.example. We'd like it to include: Lakefront Cabin Rentals, Floating Vacation Homes, and New Slips Summer 2022. We'd like it to be simple using the colors on our logo, similar to our business cards, and have our logo on it large. Maybe an arrow on the bottom pointing left that says 3 miles, possibly our website and phone number.

Target Market(s)

Lake People, Boaters

Industry/Entity Type

Resort & Marina (Recreation/Hospitality)

Font styles to use
Sans Serif
Other font styles liked:
• Simple/modern

Colors
0054AA
0677BA
7BADD7
CADEEF
E8F1F8
FFC000
F8CF3A
FAE287
FDF2CF
FEFAEE
F0912C
F2A743
F7CA91
FBE8D2
FDF5EE

Requirements
Must have
• Logo, Cabin Rentals, Floating Vacation Homes, New Slips Summer 2022
Nice to have
• An additional banner hanging from the bottom with an orange (or blue, colors from our logo) arrow pointing left, with white text saying: 3 miles 555-214-0867 www.copperridgeresort.example
Should not have
• Shouldn't be too busy

```html
<!DOCTYPE html>
<html lang="en">
<head>
<meta charset="utf-8">
<title>Copper Ridge Resort &amp; Marina Billboard</title>
<link href="https://fonts.googleapis.com/css2?family=Fira+Sans+Condensed:wght@500&family=Montserrat:wght@800&family=Saira+Semi+Condensed:wght@600;700&display=swap" rel="stylesheet">
<style>
  :root {
    --navy: #123466;
    --blue-text: #23569a;
    --band-blue: #2a5aa0;
    --sun-yellow: #fbb93a;
    --white: #ffffff;
    --page: #eef3f7;
    --map-tone: #e8f1f8;
  }
  * { margin: 0; padding: 0; box-sizing: border-box; }
  html, body { width: 1200px; height: 900px; overflow: hidden; }
  body { background: var(--page); position: relative; }

  .billboard {
    position: absolute; left: 40px; top: 170px;
    width: 1120px; height: 560px; overflow: hidden;
  }
  .billboard-shapes { position: absolute; inset: 0; }

  .brand {
    position: absolute; left: 70px; top: 30px; width: 400px;
    text-align: center;
    font-family: "Saira Semi Condensed", sans-serif; font-weight: 700;
    color: var(--blue-text);
  }
  .brand-dot {
    width: 44px; height: 44px; border-radius: 50%;
    background: var(--sun-yellow); margin: 0 auto 8px;
  }
  .brand-name { font-size: 34px; line-height: 1.05; letter-spacing: 1px; text-transform: uppercase; }
  .brand-name small { display: block; font-size: 20px; letter-spacing: 4px; }

  .feature-list {
    position: absolute; left: 44px; top: 175px; list-style: none;
    font-family: "Fira Sans Condensed", sans-serif; font-weight: 500;
    font-size: 50px; color: var(--blue-text);
  }
  .feature-list li { display: flex; align-items: center; height: 86px; }
  .feature-list li::before {
    content: ""; width: 16px; height: 16px; border-radius: 50%;
    background: var(--sun-yellow); margin-right: 8px; flex: none;
  }

  .lake-title {
    position: absolute; left: 643px; top: 66px;
    font-family: "Saira Semi Condensed", sans-serif; font-weight: 700;
    font-size: 36px; color: var(--sun-yellow);
  }
  .lake-map {
    position: absolute; left: 720px; top: 40px; width: 350px; height: 380px;
    border-radius: 40% 30% 45% 35%;
    background: radial-gradient(ellipse at center, rgba(232,241,248,0.35), rgba(232,241,248,0.08) 70%, transparent 75%);
  }
  .north-arrow { position: absolute; left: 700px; top: 318px; }
  .address {
    position: absolute; left: 826px; top: 343px;
    display: flex; gap: 8px; align-items: flex-start;
    font-family: "Saira Semi Condensed", sans-serif; font-weight: 600;
    font-size: 17px; line-height: 1.45; color: var(--sun-yellow);
  }

  .info-band {
    position: absolute; left: 0; top: 472px; width: 1120px; height: 88px;
    display: flex; align-items: center; color: var(--white);
    font-family: "Saira Semi Condensed", sans-serif; font-weight: 600;
  }
  .distance {
    position: absolute; left: 106px;
    font-family: "Montserrat", sans-serif; font-weight: 800; font-size: 40px;
  }
  .contact { position: absolute; display: flex; align-items: center; gap: 8px; font-size: 28px; }
  .contact-phone { left: 348px; }
  .contact-web { left: 636px; font-size: 26px; }
</style>
</head>
<body>
  <div class="billboard">
    <svg class="billboard-shapes" viewBox="0 0 1120 560" width="1120" height="560" aria-hidden="true">
      <rect width="1120" height="560" fill="var(--navy)"/>
      <path d="M0 0 H562 C552 200 610 380 714 472 H0 Z" fill="var(--sun-yellow)"/>
      <path d="M0 0 H548 C542 210 575 390 651 466 H0 Z" fill="var(--white)"/>
      <rect x="154" y="464" width="560" height="8" fill="var(--sun-yellow)"/>
      <polygon points="0,536 154,414 154,430 0,552" fill="var(--sun-yellow)"/>
      <polygon points="0,552 154,430 154,472 1120,472 1120,560 0,560" fill="var(--band-blue)"/>
    </svg>

    <div class="brand">
      <div class="brand-dot"></div>
      <div class="brand-name">Copper Ridge<small>Resort &amp; Marina</small></div>
    </div>

    <ul class="feature-list">
      <li>Lakefront Cabin Rentals</li>
      <li>Floating Vacation Homes</li>
      <li>New Slips Summer 2022</li>
    </ul>

    <div class="lake-title">Lake Texoma</div>
    <div class="lake-map" role="img" aria-label="Outline map of Lake Texoma showing the resort location"></div>

    <svg class="north-arrow" width="30" height="64" viewBox="0 0 30 64" aria-label="North">
      <text x="15" y="16" text-anchor="middle" font-family="Saira Semi Condensed, sans-serif" font-weight="700" font-size="18" fill="var(--sun-yellow)">N</text>
      <path d="M15 24 L28 60 L15 50 L2 60 Z" fill="none" stroke="var(--sun-yellow)" stroke-width="3" stroke-linejoin="round"/>
      <path d="M15 24 L15 50 L2 60 Z" fill="var(--sun-yellow)"/>
    </svg>

    <div class="address">
      <svg width="24" height="32" viewBox="0 0 24 32" aria-hidden="true">
        <path d="M12 1 C5.5 1 1 5.8 1 11.5 C1 19 12 31 12 31 C12 31 23 19 23 11.5 C23 5.8 18.5 1 12 1 Z" fill="var(--sun-yellow)"/>
        <circle cx="12" cy="11.5" r="4.5" fill="var(--navy)"/>
      </svg>
      <div>48 Harbor Point Road<br>Cedar Bend, TX 75999</div>
    </div>

    <div class="info-band">
      <span class="distance">3 MILES</span>
      <span class="contact contact-phone">
        <svg width="38" height="38" viewBox="0 0 38 38" aria-hidden="true">
          <circle cx="19" cy="19" r="18" fill="var(--sun-yellow)"/>
          <path d="M9 17 C9 11 29 11 29 17 L25 18 L24 15 C21 14 17 14 14 15 L13 18 Z" fill="var(--navy)"/>
          <path d="M14 19 H24 L27 27 H11 Z" fill="var(--navy)"/>
        </svg>
        (555) 214-0867
      </span>
      <span class="contact contact-web">
        <svg width="38" height="38" viewBox="0 0 38 38" aria-hidden="true">
          <circle cx="19" cy="19" r="18" fill="var(--sun-yellow)"/>
          <g fill="none" stroke="var(--navy)" stroke-width="2">
            <circle cx="19" cy="19" r="11"/>
            <ellipse cx="19" cy="19" rx="5" ry="11"/>
            <path d="M8 19 H30 M10 13 H28 M10 25 H28"/>
          </g>
        </svg>
        www.copperridgeresort.example
      </span>
    </div>
  </div>
</body>
</html>
```